Business Card Design Project_Velmora&Co

Hi,

We need some business cards designed that match the branding of this website: www.velmoraandco-example.com

They should match this branding and include a field for:

Name
Title
Email
Mobile number
Web Address

```html
<!DOCTYPE html>
<html lang="en">
<head>
<meta charset="utf-8">
<title>Velmora &amp; Co — Business Card</title>
<link href="https://fonts.googleapis.com/css2?family=Jost:wght@400;600&display=swap" rel="stylesheet">
<style>
  :root {
    --backdrop: #a4a5a9;
    --card: #ffffff;
    --ink: #111111;
    --chain: #9a9a9a;
  }
  * { margin: 0; padding: 0; box-sizing: border-box; }
  html, body {
    width: 1200px;
    height: 961px;
    overflow: hidden;
    background: var(--backdrop);
    font-family: "Jost", "Helvetica Neue", Arial, sans-serif;
    color: var(--ink);
  }
  .business-card {
    position: absolute;
    left: 84px;
    top: 152px;
    width: 1029px;
    height: 656px;
    background: var(--card);
    overflow: hidden;
  }
  .chain-band {
    position: absolute;
    top: 140px;
    height: 10px;
    background: var(--chain);
  }
  .chain-band--left { left: 0; width: 325px; }
  .chain-band--right { left: 703px; width: 326px; }
  .brand-name {
    position: absolute;
    left: 325px;
    width: 378px;
    top: 118px;
    text-align: center;
    font-size: 40px;
    font-weight: 600;
    letter-spacing: 1.5px;
    line-height: 54px;
    white-space: nowrap;
    color: var(--ink);
  }
  .holder {
    position: absolute;
    left: 78px;
    top: 322px;
    white-space: nowrap;
  }
  .holder-name {
    font-size: 40px;
    font-weight: 600;
    line-height: 52px;
  }
  .holder-title {
    font-size: 35px;
    font-weight: 400;
    line-height: 50px;
  }
  .contact-list {
    position: absolute;
    right: 56px;
    top: 460px;
    list-style: none;
  }
  .contact-item {
    display: flex;
    align-items: center;
    height: 48px;
    font-size: 28px;
    font-weight: 400;
    white-space: nowrap;
  }
  .contact-badge {
    width: 34px;
    height: 34px;
    margin-right: 20px;
    border-radius: 50%;
    background: var(--ink);
    color: var(--card);
    font-size: 15px;
    font-weight: 600;
    display: flex;
    align-items: center;
    justify-content: center;
    flex-shrink: 0;
  }
</style>
</head>
<body>
  <main class="business-card">
    <div class="chain-band chain-band--left" role="img" aria-label="Fine diamond chain border line"></div>
    <div class="chain-band chain-band--right" role="img" aria-label="Fine diamond chain border line"></div>
    <div class="brand-name">VELMORA &amp; CO</div>

    <section class="holder">
      <h1 class="holder-name">Maren Holt</h1>
      <p class="holder-title">Sales Manager</p>
    </section>

    <ul class="contact-list">
      <li class="contact-item"><span class="contact-badge">M</span>(12) 555.014.382</li>
      <li class="contact-item"><span class="contact-badge">E</span>maren.h@velmoraandco-example.com</li>
      <li class="contact-item"><span class="contact-badge">W</span>www.velmoraandco-example.com</li>
    </ul>
  </main>
</body>
</html>
```